The Harborline LLC Asset Classes

I'm looking for for two designs here to go into powerpoint and potentially as a standalone PDF. My company does wealth management.
Graphic Image #1
I break down the investment world into 4 broad categories
-Preservation
-Capital Markets
-Real Estate
-Alternatives
In each broad category, there are subcategories:
Preservation: cash, checking/savings accounts, money market accounts, CD's, and fixed annuities.
Capital Markets: Publicly traded stocks and bonds
Real Estate: single-family residence, retail, industrial, multifamily, and office
Alternatives: private equity, private credit, cryptocurrency, asset-backed loans, tax liens, oil & gas, litigation finance, and royalties
Graphic 2: Please see the bottom f page 1 of the Tidewater Slides PDF.
Just like in graphic one, you have 4 categories of the Capital Markets and their respective subcategories
Category 1: Domestic Stocks: Subcategories are Large, mid, and small size companies
Category 2: International Stocks: Subcategories are Large, Mid/Small and by region - Developed and Emerging
Category 3: Fixed Income: You have subcategories like corporate, municipal, government, domestic, international
Category 4: Alternatives: The subcategories are metals and real estate
---------------------
I'm looking to create a graphic (either pie chart, or a circle broken into parts or some other clever way to illustrate this) to clearly illustrate both of these universes in a clean, professional, slick manner.
Target Market(s)
Investors
Colors
Designer to choose colors to be used in the design.
Requirements
Must have
- Clean
- professional
- Easy to read
- Creative
- Visually appealling
Nice to have
- I have attached my logo and some marketing materials so you can get a feel of what I am doing. Maybe you can clean this up too!

```html
<!DOCTYPE html>
<html lang="en">
<head>
<meta charset="utf-8">
<title>Asset Classes</title>
<link rel="stylesheet" href="https://fonts.googleapis.com/css2?family=Montserrat:ital,wght@0,600;0,700;1,700&display=swap">
<style>
  :root {
    --preservation: #5b8ac6;
    --capital: #f4924a;
    --realestate: #12944a;
    --alternatives: #a87d50;
    --line: #555555;
    --bg: #ffffff;
    --text: #ffffff;
  }
  html, body {
    margin: 0;
    padding: 0;
    overflow: hidden;
    background: var(--bg);
  }
  .asset-map {
    position: relative;
    width: 1200px;
    height: 800px;
    overflow: hidden;
    background: var(--bg);
    font-family: "Montserrat", Arial, sans-serif;
    color: var(--text);
  }
  .connectors {
    position: absolute;
    inset: 0;
  }
  .category-label {
    font-family: "Montserrat", Arial, sans-serif;
    font-weight: 700;
    fill: var(--text);
    letter-spacing: 0.5px;
  }
  .category-label .emphasis { font-style: italic; }
  .sub {
    position: absolute;
    display: flex;
    align-items: center;
    justify-content: center;
    text-align: center;
    font-weight: 700;
    line-height: 1.3;
    box-sizing: border-box;
    padding: 0 6px;
    letter-spacing: 0.4px;
  }
  .sub--preservation { background: var(--preservation); left: 38px; width: 220px; height: 50px; }
  .sub--realestate { background: var(--realestate); left: 934px; width: 220px; height: 50px; }
  .sub--capital { background: var(--capital); left: 465px; top: 86px; width: 221px; height: 50px; font-size: 14px; font-weight: 600; }
  .sub--alternatives { background: var(--alternatives); width: 144px; height: 50px; font-size: 14px; font-weight: 600; }
  .sub--lg { font-size: 22px; }
  .sub--md { font-size: 16px; font-weight: 600; }
</style>
</head>
<body>
<main class="asset-map">
  <svg class="connectors" width="1200" height="800" viewBox="0 0 1200 800">
    <g class="connector-lines" stroke="var(--line)" stroke-width="1.3" fill="none">
      <line x1="586" y1="159" x2="586" y2="200"/>
      <line x1="290" y1="287" x2="290" y2="513"/>
      <line x1="290" y1="399" x2="330" y2="399"/>
      <line x1="894" y1="288" x2="894" y2="510"/>
      <line x1="854" y1="399" x2="894" y2="399"/>
      <line x1="226" y1="622" x2="966" y2="622"/>
      <line x1="592" y1="580" x2="592" y2="622"/>
    </g>

    <g class="category-circles">
      <circle cx="592" cy="292" r="94" fill="var(--capital)"/>
      <circle cx="422" cy="394" r="94" fill="var(--preservation)"/>
      <circle cx="761" cy="394" r="94" fill="var(--realestate)"/>
      <circle cx="592" cy="488" r="94" fill="var(--alternatives)"/>
    </g>

    <g class="category-labels">
      <text class="category-label" x="592" y="285" font-size="23" text-anchor="middle">Capital</text>
      <text class="category-label" x="592" y="314" font-size="23" text-anchor="middle"><tspan class="emphasis">Markets</tspan></text>
      <text class="category-label" x="422" y="403" font-size="23" text-anchor="middle">Preservation</text>
      <text class="category-label" x="763" y="403" font-size="23" text-anchor="middle">Real Estate</text>
      <text class="category-label" x="592" y="495" font-size="22" text-anchor="middle">Alternatives</text>
    </g>

    <g class="node-dots">
      <circle cx="586" cy="159" r="9.5" fill="var(--capital)"/>
      <g fill="var(--preservation)">
        <circle cx="290" cy="287" r="9.5"/>
        <circle cx="290" cy="343" r="9.5"/>
        <circle cx="290" cy="399" r="9.5"/>
        <circle cx="290" cy="456" r="9.5"/>
        <circle cx="290" cy="513" r="9.5"/>
      </g>
      <g fill="var(--realestate)">
        <circle cx="894" cy="288" r="9.5"/>
        <circle cx="894" cy="345" r="9.5"/>
        <circle cx="894" cy="399" r="9.5"/>
        <circle cx="894" cy="457" r="9.5"/>
        <circle cx="894" cy="510" r="9.5"/>
      </g>
      <g fill="var(--alternatives)">
        <circle cx="226" cy="622" r="9.5"/>
        <circle cx="376" cy="622" r="9.5"/>
        <circle cx="524" cy="620" r="9.5"/>
        <circle cx="670" cy="620" r="9.5"/>
        <circle cx="817" cy="621" r="9.5"/>
        <circle cx="966" cy="622" r="9.5"/>
      </g>
    </g>
  </svg>

  <div class="sub sub--capital">Publicly traded stocks and bonds</div>

  <div class="sub sub--preservation sub--lg" style="top:262px">Cash</div>
  <div class="sub sub--preservation sub--md" style="top:318px">checking/savings accounts</div>
  <div class="sub sub--preservation sub--md" style="top:374px">money market accounts</div>
  <div class="sub sub--preservation sub--lg" style="top:431px">CD's</div>
  <div class="sub sub--preservation sub--lg" style="top:488px">fixed annuities</div>

  <div class="sub sub--realestate sub--md" style="top:263px">single-family residence</div>
  <div class="sub sub--realestate sub--lg" style="top:319px">retail</div>
  <div class="sub sub--realestate sub--lg" style="top:375px">industrial</div>
  <div class="sub sub--realestate sub--lg" style="top:432px">multifamily</div>
  <div class="sub sub--realestate sub--lg" style="top:489px">office</div>

  <div class="sub sub--alternatives" style="left:52px; top:597px">private equity</div>
  <div class="sub sub--alternatives" style="left:1001px; top:596px">private equity</div>
  <div class="sub sub--alternatives" style="left:157px; top:654px">private credit</div>
  <div class="sub sub--alternatives" style="left:305px; top:654px">cryptocurrency</div>
  <div class="sub sub--alternatives" style="left:453px; top:654px; font-size:12.5px">asset-backed loans</div>
  <div class="sub sub--alternatives" style="left:598px; top:654px">tax liens</div>
  <div class="sub sub--alternatives" style="left:746px; top:654px">oil &amp; gas</div>
  <div class="sub sub--alternatives" style="left:894px; top:654px">litigation finance</div>
</main>
</body>
</html>
```